Tovimerra: Travel business card redesign

We need a clean elegant look for our cards featuring blue and orange. Look should communicate a sense of strong design and seem uncluttered. The company is Tovimerra which means escape to bliss. As in every trip is an escape to bliss. Feel free to reinvent the logo or just tweak it. Colors should be blue like Caribbean waters and a saturated orange. Keep it clean and simple.
Please match the information in the sample uploaded but the sample is horrible -- a non-starter -- use for information only. also please add managing director to my name as title

Target Market(s)
potential clients, hotels, trade publications
Industry/Entity Type
Travel Industry
Contact Information for Business Card
as above
Requirements
Must have
- Font should be century gothic. Colors below are close but a but prefer lighter in each case.

```html
<!DOCTYPE html>
<html lang="en">
<head>
<meta charset="utf-8">
<title>Tovimerra Business Cards</title>
<link href="https://fonts.googleapis.com/css2?family=Didact+Gothic&display=swap" rel="stylesheet">
<style>
  :root {
    --orange: #ef8c2f;
    --blue: #79abd3;
    --paper: #f4f4f4;
    --ink: #555555;
    --rule: #b9b9b9;
    --backdrop: #e6e3df;
  }
  * { box-sizing: border-box; margin: 0; padding: 0; }
  html, body { width: 1200px; height: 886px; overflow: hidden; }
  body {
    background: var(--backdrop);
    font-family: "Didact Gothic", "Century Gothic", sans-serif;
    position: relative;
  }
  .card {
    position: absolute;
    width: 560px;
    height: 320px;
    border-radius: 22px;
    overflow: hidden;
    box-shadow: 0 10px 26px rgba(0,0,0,0.18);
  }
  .card-front {
    left: 60px; top: 110px;
    background: var(--orange);
    color: #fff;
    text-align: center;
  }
  .card-front .wordmark {
    position: absolute; left: 0; right: 0; top: 110px;
    font-size: 64px; letter-spacing: -1px;
  }
  .card-front .tagline {
    position: absolute; left: 0; right: 0; bottom: 56px;
    font-size: 17px; letter-spacing: 0.5px;
  }
  .card-back {
    left: 580px; top: 440px;
    background: var(--paper);
  }
  .card-back .wordmark {
    position: absolute; left: 34px; top: 112px; width: 240px;
    font-size: 44px; color: var(--orange); letter-spacing: -1px;
  }
  .card-back .divider {
    position: absolute; left: 290px; top: 50px;
    width: 1px; height: 180px; background: var(--rule);
  }
  .details { position: absolute; left: 312px; top: 62px; width: 240px; color: var(--ink); }
  .details .name { color: var(--orange); font-size: 21px; letter-spacing: 1px; }
  .details .title { color: var(--blue); font-size: 14px; letter-spacing: 1.5px; margin-top: 2px; }
  .details .address { font-size: 14px; line-height: 1.35; margin-top: 14px; }
  .contact { list-style: none; margin-top: 8px; font-size: 14px; line-height: 1.4; }
  .contact li { display: flex; align-items: center; gap: 8px; }
  .contact svg { width: 12px; height: 12px; flex: none; }
  .card-back .band {
    position: absolute; left: 0; right: 0; bottom: 0; height: 24px;
    display: flex;
  }
  .band .band-orange { flex: 0 0 72%; background: var(--orange); }
  .band .band-blue { flex: 1; background: var(--blue); }
</style>
</head>
<body>
  <section class="card card-front">
    <div class="wordmark">tovimerra</div>
    <div class="tagline">A first in service company</div>
  </section>

  <section class="card card-back">
    <div class="wordmark">tovimerra</div>
    <div class="divider"></div>
    <div class="details">
      <div class="name">DARA LINDQVIST</div>
      <div class="title">MANAGING DIRECTOR</div>
      <div class="address">4417 Harbor Crest Way<br>Ventura, 93001</div>
      <ul class="contact">
        <li>
          <svg viewBox="0 0 12 12"><path d="M2 1h2.5l1 2.5-1.4 1a6 6 0 0 0 3.4 3.4l1-1.4L11 7.5V10a1 1 0 0 1-1 1C5 11 1 7 1 2a1 1 0 0 1 1-1z" fill="#ef8c2f"/></svg>
          877.86.TOVIM (868846)
        </li>
        <li>
          <svg viewBox="0 0 12 12"><rect x="3" y="0.7" width="6" height="10.6" rx="1" fill="none" stroke="#ef8c2f" stroke-width="1.3"/><circle cx="6" cy="9.4" r="0.7" fill="#ef8c2f"/></svg>
          323.555.0148
        </li>
        <li>
          <svg viewBox="0 0 12 12"><rect x="3" y="1" width="6" height="3" fill="#ef8c2f"/><rect x="1" y="4.5" width="10" height="5" rx="1" fill="#ef8c2f"/><rect x="3" y="8" width="6" height="3" fill="#f4f4f4" stroke="#ef8c2f"/></svg>
          310.555.0193
        </li>
      </ul>
    </div>
    <div class="band"><div class="band-orange"></div><div class="band-blue"></div></div>
  </section>
</body>
</html>
```